Modern and professional facebook ad for disability service

Design a facebook ad for a disability service. Want something bright and fun and eyecatching. Would ideally like a carousel ad as this will give us more options to provide information.
CONTENT:
- Looking for a Plan Manager who will support your QRTA journey so that you can focus on living your best possible life and achieve your QRTA Goals?
- Then join the Bluegate Plan Management family today - quick and easy sign up.
- Friendly, Reliable, Responsive Service
- Dedicate Plan Managers so you always speak to the same person
- Fast Payment of Provider Invoices
- Supporting you to live Your Life, Your Way
- Call us today on 1300 482 613
- www.bluegateplanmanagement.com.au

Target Market(s)

Disability Sector

Other font styles liked:
• Raleway

Requirements
Must have
• Bright colours and eye catching design

```html
<!DOCTYPE html>
<html lang="en">
<head>
<meta charset="utf-8">
<title>Bluegate Plan Management – Carousel Ad</title>
<link rel="stylesheet" href="https://fonts.googleapis.com/css2?family=Playfair+Display:wght@700&family=Great+Vibes&family=Poppins:wght@500;700&display=swap">
<style>
  :root{
    --bg:#c5dedf;
    --teal:#0f8380;
    --magenta:#ab3268;
    --white:#ffffff;
    --badge:#4b3c7a;
    --serif:"Playfair Display", Georgia, serif;
    --script:"Great Vibes", cursive;
    --sans:"Poppins", Arial, sans-serif;
  }
  *{box-sizing:border-box;margin:0;padding:0}
  html,body{width:1200px;height:800px;overflow:hidden;background:var(--bg)}
  .carousel{position:absolute;left:15px;top:255px;width:1170px;height:290px;display:flex;gap:10px}
  .spread{position:relative;width:580px;height:290px;background:var(--teal);overflow:hidden;box-shadow:0 8px 14px rgba(0,0,0,.12)}
  .spread .waves{position:absolute;inset:0}
  .photo-frame{position:absolute;left:173px;top:7px;width:228px;height:265px;border:1.5px solid var(--white);border-radius:26px}
  .photo{position:absolute;left:179px;top:13px;width:222px;height:265px;border-radius:22px}
  .photo--office{background:linear-gradient(160deg,#d9d6cf 0%,#a89a86 45%,#6f5a45 100%)}
  .photo--laptop{background:linear-gradient(160deg,#6fb3b0 0%,#d8cbb8 55%,#b9b3ad 100%)}
  .badge{position:absolute;left:24px;top:213px;width:58px;height:58px;border-radius:50%;background:var(--badge);border:2px solid var(--white)}
  .lead{position:absolute;color:var(--white);font-family:var(--serif);font-weight:700}
  .lead--question{left:25px;top:21px;width:150px;font-size:13.5px;line-height:16px}
  .lead--join{right:28px;top:20px;width:150px;text-align:right;font-size:20px;line-height:24px}
  .lead--dedicated{left:26px;top:26px;width:150px;font-size:13.5px;line-height:17.5px}
  .lead--values{right:27px;top:24px;text-align:right;font-size:23px;line-height:27px}
  .script{font-family:var(--script);font-weight:400;color:var(--white)}
  .lead--join .script{display:block;font-size:21px;line-height:26px;margin-top:2px}
  .lead--dedicated .script{display:block;font-size:24px;line-height:26px}
  .lead--values .script{display:block;font-size:44px;line-height:44px;margin-top:2px;padding-right:2px}
  .contact{position:absolute;right:28px;top:224px;text-align:right;color:var(--white);font-family:var(--sans)}
  .contact__call{font-size:12.5px;font-weight:500;line-height:15px}
  .contact__phone{display:flex;align-items:center;justify-content:flex-end;gap:3px;font-size:18.5px;font-weight:700;line-height:20px}
  .contact__phone svg{width:13px;height:13px}
  .contact__site{display:flex;margin-top:3px;height:13px;font-size:6.5px;line-height:13px}
  .contact__visit{background:var(--white);color:var(--magenta);font-weight:700;padding:0 4px}
  .contact__url{background:var(--teal);color:var(--white);font-weight:500;font-size:3.6px;padding:0 3px;border:1px solid var(--white)}
</style>
</head>
<body>
<main class="carousel" aria-label="Bluegate Plan Management carousel ad">

  <section class="spread spread--join">
    <svg class="waves" viewBox="0 0 580 290" aria-hidden="true">
      <path d="M0,188 C70,158 140,190 230,262 L360,262 C440,200 500,160 580,176 V290 H0Z" fill="var(--magenta)"/>
      <path d="M0,180 C70,150 140,182 230,254 M360,254 C440,192 500,152 580,168" fill="none" stroke="var(--white)" stroke-width="3"/>
    </svg>
    <div class="badge" aria-label="Partner badge"></div>
    <p class="lead lead--question">Looking for a Plan Manager who will support your QRTA journey so that you can focus on living your best possible life and achieve your QRTA Goals?</p>
    <div class="photo-frame"></div>
    <div class="photo photo--office" role="img" aria-label="Photo: two women laughing together at a meeting table in an office"></div>
    <p class="lead lead--join">Then join the Bluegate Plan Management family today
      <span class="script">Quick and<br>Easy Sign Up</span></p>
    <div class="contact">
      <p class="contact__call">Call us today on</p>
      <p class="contact__phone"><svg viewBox="0 0 24 24" aria-hidden="true"><circle cx="12" cy="12" r="10.5" fill="none" stroke="#fff" stroke-width="2"/><path d="M8 6.5c-1 .6-1.6 1.8-1 3.4 1 2.7 3.4 5.3 6.3 6.6 1.5.6 2.7 0 3.3-1l-2-2-1.6.9c-1.3-.7-2.5-1.9-3.2-3.2l.9-1.6z" fill="#fff"/></svg>1300 482 613</p>
      <p class="contact__site"><span class="contact__visit">Visit Our Site</span><span class="contact__url">www.bluegateplanmanagement.com.au</span></p>
    </div>
  </section>

  <section class="spread spread--values">
    <svg class="waves" viewBox="0 0 580 290" aria-hidden="true">
      <path d="M0,188 C70,158 140,190 230,262 L360,262 C440,200 500,160 580,176 V290 H0Z" fill="var(--magenta)"/>
      <path d="M0,180 C70,150 140,182 230,254 M360,254 C440,192 500,152 580,168" fill="none" stroke="var(--white)" stroke-width="3"/>
    </svg>
    <div class="badge" aria-label="Partner badge"></div>
    <p class="lead lead--dedicated">Dedicate Plan Managers so you always speak to the
      <span class="script">same person</span></p>
    <div class="photo-frame"></div>
    <div class="photo photo--laptop" role="img" aria-label="Photo: a plan manager and a client smiling while looking at a laptop together"></div>
    <p class="lead lead--values">Friendly,<br>Reliable,<br>Responsive
      <span class="script">Service</span></p>
    <div class="contact">
      <p class="contact__call">Call us today on</p>
      <p class="contact__phone"><svg viewBox="0 0 24 24" aria-hidden="true"><circle cx="12" cy="12" r="10.5" fill="none" stroke="#fff" stroke-width="2"/><path d="M8 6.5c-1 .6-1.6 1.8-1 3.4 1 2.7 3.4 5.3 6.3 6.6 1.5.6 2.7 0 3.3-1l-2-2-1.6.9c-1.3-.7-2.5-1.9-3.2-3.2l.9-1.6z" fill="#fff"/></svg>1300 482 613</p>
      <p class="contact__site"><span class="contact__visit">Visit Our Site</span><span class="contact__url">www.bluegateplanmanagement.com.au</span></p>
    </div>
  </section>

</main>
</body>
</html>
```